Real Estate Entrepreneur needs a business card

I am a real estate entrepreneur, I buy houses for investment purposes, I act as a real estate agent representing buyers and sellers in residential home transactions, I am a contractor that does a wide range of home repairs and construction. I'd like a design that can stick with me through the years as my business grows and morphs to fit any niche I decide to pursue as markets change.

Target Market(s)

Anyone with interest that may be related to real estate.

Industry/Entity Type

Real Estate

Contact Information for Business Card

A card that stands out and doesn't put me in any one box. My business will evolve over time and I need a card that can stay relevant.

Colors

Designer to choose colors to be used in the design.

Requirements
Must have
• Character
Nice to have
• I'm open
Should not have
• Cliche houses and hammers

```html
<!DOCTYPE html>
<html lang="en">
<head>
<meta charset="utf-8">
<title>Wade Hale — Business Card</title>
<link rel="stylesheet" href="https://fonts.googleapis.com/css2?family=Montserrat:wght@400;600&display=swap">
<style>
  :root {
    --backdrop: #222222;
    --card: #252626;
    --accent: #0ba6d2;
    --text: #e9ecee;
    --shadow: rgba(0, 0, 0, 0.55);
  }
  * { margin: 0; padding: 0; box-sizing: border-box; }
  html, body {
    width: 1200px;
    height: 549px;
    overflow: hidden;
    background: var(--backdrop);
    font-family: "Montserrat", sans-serif;
  }
  .stage { position: relative; width: 1200px; height: 549px; }
  .card {
    position: absolute;
    top: 130px;
    width: 507px;
    height: 289px;
    background: var(--card);
    box-shadow: 0 14px 30px var(--shadow);
    overflow: hidden;
  }
  .card--front { left: 78px; }
  .card--back { left: 615px; }
  .name-part {
    position: absolute;
    bottom: 10px;
    font-weight: 600;
    font-size: 81px;
    line-height: 1;
    letter-spacing: -0.5px;
    color: var(--accent);
  }
  .card--front .name-part { right: 20px; }
  .card--back .name-part { left: 16px; }
  .contact-list {
    position: absolute;
    top: 21px;
    left: 332px;
    list-style: none;
  }
  .contact-item {
    display: flex;
    align-items: center;
    height: 20.5px;
    font-size: 12.5px;
    color: var(--text);
  }
  .contact-icon {
    width: 14px;
    height: 14px;
    margin-right: 9px;
    fill: var(--accent);
    stroke: var(--accent);
  }
  .social {
    position: absolute;
    left: 332px;
    bottom: 20px;
    display: flex;
    align-items: center;
    font-size: 12.5px;
    color: var(--text);
  }
  .social-dot {
    width: 13px;
    height: 13px;
    border-radius: 50%;
    background: var(--accent);
    margin-right: 8px;
  }
</style>
</head>
<body>
<div class="stage">
  <section class="card card--front">
    <span class="name-part">Wade</span>
  </section>

  <section class="card card--back">
    <ul class="contact-list">
      <li class="contact-item">
        <svg class="contact-icon" viewBox="0 0 14 14" aria-hidden="true">
          <path stroke="none" d="M1 5 C1 2.5 13 2.5 13 5 L13 6 L10 6 L10 4.8 L4 4.8 L4 6 L1 6 Z"/>
          <path stroke="none" d="M3.5 7 L10.5 7 L12 12 L2 12 Z"/>
        </svg>
        (555) 204 - 3170
      </li>
      <li class="contact-item">
        <svg class="contact-icon" viewBox="0 0 14 14" aria-hidden="true">
          <rect x="3.5" y="0.8" width="7" height="12.4" rx="1.2" fill="none" stroke-width="1.5"/>
          <rect x="6" y="10.6" width="2" height="1" stroke="none"/>
        </svg>
        (555) 318 - 6642
      </li>
      <li class="contact-item">
        <svg class="contact-icon" viewBox="0 0 14 14" aria-hidden="true">
          <rect x="0.5" y="2.5" width="13" height="9" stroke="none"/>
          <path d="M0.8 2.8 L7 8 L13.2 2.8" fill="none" stroke="#252626" stroke-width="1.2"/>
        </svg>
        info@wadehale.com
      </li>
      <li class="contact-item">
        <svg class="contact-icon" viewBox="0 0 14 14" aria-hidden="true">
          <circle cx="7" cy="7" r="6" stroke="none"/>
          <g fill="none" stroke="#252626" stroke-width="0.9">
            <ellipse cx="7" cy="7" rx="2.6" ry="6"/>
            <line x1="1" y1="7" x2="13" y2="7"/>
            <line x1="2" y1="4" x2="12" y2="4"/>
            <line x1="2" y1="10" x2="12" y2="10"/>
          </g>
        </svg>
        www.wadehale.com
      </li>
    </ul>

    <span class="name-part">Hale</span>

    <div class="social">
      <span class="social-dot" aria-hidden="true"></span>
      / wadehale
    </div>
  </section>
</div>
</body>
</html>
```